依頼詳細
(例)毎年忘年会・新年会チラシをうちます。その広告デザインをお願い致します。今年は新企画として女子会プランを紙面の半分のスペースに入れたいと思います。明るく楽しく見やすい和のデザインをお願いします。
記載項目
(例)入る原稿(文字、写真)はイラストレーターCS2にて添付します。裏面は昨年から流用しますので表面には住所や地図は入りません。タイトルをいじったりキャッチコピーを入れて下さってかまいません。
希望イメージ
シンプル 複雑
単色 カラフル
暗い 明るい
日常 高級
遊び心 厳粛
未来的 伝統的
女性的 男性的
希望する色
(例)赤、黒(特にこだわりません)
納品ファイル
• 高解像度JPG (.jpg)
• イラストレーター形式 (.ai)
補足説明
■ 選んだ理由

明るく楽しげな雰囲気がとてもよかったです。女子会のタイトルの工夫もいい感じです。

■ 提案者全員のお礼・コメント

多くの方に提案して頂きありがとうございました。1つ選ぶのは心苦しいのですが選んだ納得感が気に入っています。またお願いするときにはよろしくお願いします。

```html
<!DOCTYPE html>
<html lang="ja">
<head>
<meta charset="utf-8">
<title>福鮨 忘年会・新年会 女子会セット</title>
<link rel="stylesheet" href="https://fonts.googleapis.com/css2?family=Shippori+Mincho+B1:wght@500;700;800&family=Noto+Sans+JP:wght@400;700;900&display=swap">
<style>
  :root{
    --red:#b8121c;
    --deep-red:#8e0d14;
    --orange:#f08a1c;
    --orange-dark:#e4531a;
    --gold:#f4c63c;
    --cream:#fdf4e0;
    --pink:#f8d8e0;
    --pink-deep:#e98aa4;
    --ink:#231815;
    --white:#ffffff;
  }
  *{margin:0;padding:0;box-sizing:border-box}
  html,body{width:849px;height:1200px;overflow:hidden;background:#fff}
  .flyer{position:relative;width:849px;height:1200px;overflow:hidden;
    background:linear-gradient(180deg,var(--orange) 0%,var(--orange-dark) 48%,var(--pink) 48%,var(--pink) 100%);
    font-family:"Noto Sans JP",sans-serif;color:var(--ink)}
  .abs{position:absolute}

  /* header */
  .brand{left:24px;top:14px;width:290px;height:130px;background:var(--white);border-radius:0 0 18px 0;
    display:flex;flex-direction:column;align-items:center;justify-content:center}
  .brand-kana{font-size:15px;font-weight:700;letter-spacing:.4em;color:var(--red)}
  .brand-name{font-family:"Shippori Mincho B1",serif;font-weight:800;font-size:78px;line-height:1;color:var(--ink);letter-spacing:.05em}
  .intro{left:330px;top:18px;width:290px;font-size:11.5px;line-height:1.7;color:var(--white);font-weight:700}

  .title-panel{left:618px;top:0;width:231px;height:272px;
    background:radial-gradient(circle at 70% 25%,#e8632a 0%,#c52a1a 55%,var(--deep-red) 100%)}
  .title-kicker{left:818px;top:10px;font-size:12px;color:var(--white);writing-mode:vertical-rl;font-weight:700;white-space:nowrap}
  .title-main{left:636px;top:16px;writing-mode:vertical-rl;font-family:"Shippori Mincho B1",serif;font-weight:800;
    font-size:56px;line-height:1.05;color:var(--white);letter-spacing:.02em;text-shadow:0 2px 0 rgba(0,0,0,.25);white-space:nowrap}
  .title-sub{left:768px;top:70px;writing-mode:vertical-rl;background:var(--gold);color:var(--deep-red);
    font-weight:900;font-size:16px;padding:8px 3px;letter-spacing:.15em;white-space:nowrap}

  .discount{left:622px;top:276px;width:205px;height:56px;background:var(--white);border:2px solid var(--red);
    display:flex;align-items:center;gap:6px;padding:0 8px}
  .discount-pct{font-size:30px;font-weight:900;color:var(--red);line-height:1;white-space:nowrap}
  .discount-pct small{font-size:16px}
  .discount-note{font-size:11px;font-weight:700;line-height:1.35}
  .group-note{left:622px;top:338px;font-size:11px;color:var(--white);font-weight:700}
  .shuttle{left:622px;top:356px;width:205px;height:72px;background:var(--cream);border:2px solid var(--red);
    display:flex;align-items:center;padding:0 8px;gap:6px}
  .shuttle-text{font-size:15px;font-weight:900;color:var(--red);line-height:1.35}
  .shuttle-art{width:66px;height:48px;border-radius:6px;background:linear-gradient(135deg,#f4f1ea,#c9c3b5)}

  /* plan cards */
  .plan{top:152px;height:274px;width:282px;background:var(--cream);border:3px solid var(--white);border-radius:6px;overflow:hidden}
  .plan-head{display:flex;align-items:center;gap:8px;padding:10px 10px 4px}
  .plan-badge{width:42px;height:42px;border-radius:50%;background:var(--red);color:var(--white);
    font-weight:900;font-size:16px;display:flex;align-items:center;justify-content:center;line-height:1}
  .plan-name{font-family:"Shippori Mincho B1",serif;font-weight:800;font-size:30px;color:var(--ink)}
  .plan-price-row{display:flex;flex-wrap:nowrap;align-items:flex-end;gap:6px;padding:0 12px}
  .plan-unit{font-size:10px;font-weight:700;background:var(--red);color:var(--white);padding:2px 6px;white-space:nowrap;margin-bottom:4px}
  .plan-price{font-size:36px;font-weight:900;color:var(--red);line-height:1;white-space:nowrap}
  .plan-price small{font-size:17px}
  .plan-list{font-size:12px;font-weight:700;padding:6px 14px 4px;line-height:1.5}
  .plan-photo{margin:4px 10px;height:118px;border-radius:4px}
  .photo-drinks{background:linear-gradient(135deg,#f3c75a,#c6761e 70%,#6b3a16)}
  .photo-pot{background:radial-gradient(circle at 50% 55%,#e7b184,#b3552c 55%,#3a2418)}

  .kaiseki-band{left:40px;top:432px;width:570px;height:38px;background:var(--red);color:var(--white);
    display:flex;align-items:center;justify-content:center;gap:12px;font-weight:900;font-size:18px}
  .kaiseki-band b{font-size:26px;color:var(--gold)}
  .kaiseki-row{left:40px;top:474px;width:570px;height:90px;display:flex;justify-content:space-between}
  .kaiseki{position:relative;width:138px;height:90px}
  .kaiseki-photo{position:absolute;right:0;top:4px;width:84px;height:84px;border-radius:50%;
    background:radial-gradient(circle,#e9c79a,#a8653a 65%,#4b2d1c);border:3px solid var(--white)}
  .kaiseki-mark{position:absolute;left:0;top:6px;width:40px;height:40px;border-radius:50%;color:var(--white);
    font-family:"Shippori Mincho B1",serif;font-weight:800;font-size:22px;display:flex;align-items:center;justify-content:center}
  .kaiseki-price{position:absolute;left:0;top:52px;font-weight:900;font-size:15px;color:var(--white);text-shadow:0 1px 2px rgba(0,0,0,.4);white-space:nowrap}
  .kaiseki-price small{font-size:10px}

  /* girls' night */
  .joshi{left:24px;top:572px;width:801px;height:610px;background:var(--white);border-radius:10px}
  .joshi-head{left:40px;top:588px;width:330px;height:96px;background:var(--red);border-radius:8px;color:var(--white);padding:10px 16px}
  .joshi-en{font-size:15px;letter-spacing:.1em;color:var(--gold);font-weight:700}
  .joshi-title{font-family:"Shippori Mincho B1",serif;font-weight:800;font-size:48px;line-height:1.1}
  .joshi-title span{font-size:28px}
  .joshi-period{left:260px;top:596px;font-size:11px;color:var(--white);font-weight:700}
  .joshi-intro{left:392px;top:596px;width:420px;font-size:12px;line-height:1.75;font-weight:700;color:var(--ink)}

  .course{top:694px;width:380px;height:476px}
  .course-catch{font-size:15px;font-weight:900;color:var(--pink-deep);text-align:center}
  .course-name{margin-top:4px;background:var(--pink-deep);color:var(--white);text-align:center;
    font-family:"Shippori Mincho B1",serif;font-weight:800;font-size:28px;padding:6px 0;border-radius:4px}
  .course-photo{margin-top:10px;height:290px;border-radius:6px}
  .photo-sushi{background:linear-gradient(135deg,#2c2624,#7b5a4a 40%,#e8b49a 70%,#f5e9dc)}
  .photo-gozen{background:radial-gradient(circle at 50% 50%,#f0c8a8,#c0392b 55%,#2b1a17)}
  .course-foot{display:flex;align-items:flex-end;justify-content:space-between;margin-top:12px}
  .course-price{font-size:46px;font-weight:900;color:var(--red);line-height:1;white-space:nowrap}
  .course-price small{font-size:14px;color:var(--ink)}
  .course-items{font-size:12px;font-weight:700;line-height:1.6;text-align:right}
</style>
</head>
<body>
<div class="flyer">

  <div class="abs brand">
    <div class="brand-kana">ふくすし</div>
    <div class="brand-name">福鮨</div>
  </div>

  <p class="abs intro">今年も残すところあとわずか。皆様の一年の労をねぎらう宴に、旬の味覚と心づくしのおもてなしをご用意しました。大切な方々と楽しいひとときをお過ごしください。</p>

  <div class="abs title-panel" role="img" aria-label="紅葉の葉が散る赤い背景"></div>
  <div class="abs title-kicker">今年もお世話になりました</div>
  <div class="abs title-main">忘年会<br>新年会</div>
  <div class="abs title-sub">ご予約承ります</div>

  <div class="abs discount">
    <div class="discount-pct">5%<small>OFF</small></div>
    <div class="discount-note">お食事券にて<br>お支払い致します</div>
  </div>
  <div class="abs group-note">15名様以上でご利用いただけます。</div>
  <div class="abs shuttle">
    <div class="shuttle-text">当店のバスで<br>送迎致します。</div>
    <div class="shuttle-art" role="img" aria-label="送迎バスの写真"></div>
  </div>

  <section class="abs plan" style="left:40px">
    <div class="plan-head"><div class="plan-badge">得々</div><div class="plan-name">飲み放題</div></div>
    <div class="plan-price-row"><span class="plan-unit">お一人様(税込)</span><span class="plan-price">5,000<small>円より</small></span></div>
    <div class="plan-list">◆お料理＋お飲み物</div>
    <div class="plan-photo photo-drinks" role="img" aria-label="ビールと宴会料理の写真"></div>
  </section>

  <section class="abs plan" style="left:328px">
    <div class="plan-head"><div class="plan-badge">冬</div><div class="plan-name">寄せ鍋</div></div>
    <div class="plan-price-row"><span class="plan-unit">お一人様(税込)</span><span class="plan-price">3,500<small>円より</small></span></div>
    <div class="plan-list">◆旬の魚介と野菜たっぷり</div>
    <div class="plan-photo photo-pot" role="img" aria-label="寄せ鍋の写真"></div>
  </section>

  <div class="abs kaiseki-band">◆法要後のお食事宴会用会席料理 <b>3,500</b>円より</div>
  <div class="abs kaiseki-row">
    <div class="kaiseki"><div class="kaiseki-mark" style="background:#d9437a">彩</div><div class="kaiseki-price">3,500<small>円</small></div><div class="kaiseki-photo" role="img" aria-label="会席料理 彩の写真"></div></div>
    <div class="kaiseki"><div class="kaiseki-mark" style="background:#c0392b">梅</div><div class="kaiseki-price">4,000<small>円</small></div><div class="kaiseki-photo" role="img" aria-label="会席料理 梅の写真"></div></div>
    <div class="kaiseki"><div class="kaiseki-mark" style="background:#4a8a3a">竹</div><div class="kaiseki-price">5,000<small>円</small></div><div class="kaiseki-photo" role="img" aria-label="会席料理 竹の写真"></div></div>
    <div class="kaiseki"><div class="kaiseki-mark" style="background:#2e5a3a">松</div><div class="kaiseki-price">7,000<small>円</small></div><div class="kaiseki-photo" role="img" aria-label="会席料理 松の写真"></div></div>
  </div>

  <div class="abs joshi"></div>
  <div class="abs joshi-head">
    <div class="joshi-en">Joshikai</div>
    <div class="joshi-title">女子会<span>セット</span></div>
  </div>
  <div class="abs joshi-period">11時～20時</div>
  <p class="abs joshi-intro">新企画スタート！女性だけのお得な「女子会セット」をご用意しました。おしゃべりしながら美味しいお料理を少しずつ楽しめる、華やかなコースです。お友達とお気軽にどうぞ。</p>

  <section class="abs course" style="left:40px">
    <div class="course-catch">やっぱりお寿司を満喫したい！</div>
    <div class="course-name">女子会上寿司コース</div>
    <div class="course-photo photo-sushi" role="img" aria-label="上寿司盛り合わせと天ぷらの写真"></div>
    <div class="course-foot">
      <div class="course-price">2,500<small>円(税込)</small></div>
      <div class="course-items">◆茶碗蒸し・天ぷら<br>◆デザート・ソフトドリンク</div>
    </div>
  </section>

  <section class="abs course" style="left:430px">
    <div class="course-catch">美味しいものをちょっとずつ。</div>
    <div class="course-name">女子会御膳コース</div>
    <div class="course-photo photo-gozen" role="img" aria-label="彩り豊かな御膳料理の写真"></div>
    <div class="course-foot">
      <div class="course-price">2,500<small>円(税込)</small></div>
      <div class="course-items">◆お刺身・小鉢・デザート<br>◆ソフトドリンク付き</div>
    </div>
  </section>

</div>
</body>
</html>
```